Display wall/splashback design

We are looking at a design to suit the background display/splashback wall of our instore showroom displays needs to be in suttle colours that do not detract from the appliances attached to this wall.
Most of the rangehoods on display are of a stainless colour hence the background cannot have strong solid colours that will attract the eye of the customer away from the products .
One of the main features of our rangehoods is their silence, so something to highlites silence/quiet would be most appropiate.
Sixe is 1.8 metres in height x 6 metres in length

Target Market(s)

High end consumer, women between 25 and 50

Industry/Entity Type

Retail

Requirements
Must have
• An overall gently/quiet and enviromentally friendly look.
A background that inhances the product displayed upon it.

Should not have
• Strong or dominant images nor strong or dominant colours

```html
<!DOCTYPE html>
<html lang="en">
<head>
<meta charset="utf-8">
<title>Showroom Splashback Wall</title>
<style>
  :root {
    --wall-mint: #e0fbec;
    --glow-pale: rgba(240, 236, 150, 1);
    --glow-mid: rgba(240, 236, 150, 0.55);
    --glow-none: rgba(240, 236, 150, 0);
    --rail-gold: #c4950f;
  }
  html, body {
    margin: 0;
    padding: 0;
    overflow: hidden;
  }
  .splashback {
    position: relative;
    width: 1200px;
    height: 444px;
    background: var(--wall-mint);
    overflow: hidden;
  }
  .rail-glow {
    position: absolute;
    left: 0;
    width: 1200px;
  }
  .rail-glow--upper {
    top: 285px;
    height: 108px;
    background: linear-gradient(to bottom,
      var(--glow-none) 0%,
      var(--glow-mid) 22%,
      var(--glow-pale) 42%,
      var(--glow-pale) 58%,
      var(--glow-mid) 72%,
      var(--glow-none) 92%);
  }
  .rail-glow--lower {
    top: 368px;
    height: 78px;
    background: linear-gradient(to bottom,
      var(--glow-none) 0%,
      var(--glow-mid) 22%,
      var(--glow-pale) 40%,
      var(--glow-pale) 60%,
      var(--glow-mid) 78%,
      var(--glow-none) 100%);
  }
  .rail {
    position: absolute;
    left: 0;
    width: 1200px;
    height: 10px;
    background: var(--rail-gold);
  }
  .rail--upper { top: 334px; }
  .rail--lower { top: 402px; }
</style>
</head>
<body>
  <div class="splashback">
    <div class="rail-glow rail-glow--upper"></div>
    <div class="rail-glow rail-glow--lower"></div>
    <div class="rail rail--upper"></div>
    <div class="rail rail--lower"></div>
  </div>
</body>
</html>
```